Website created on Plinkora.com

I have a telecommunications company and i would like my website built on plinkora.com as this platform is easy for me to change in the future so the site needs to be made so i can change it when i need to. Also I have found Plinkora is very good for SEO setup
Examples of websites i like as they are clean and corporate www.tarnocall.com.au (on this site there are menus on the right hand side which changes the content on the same page I would like the also www.quelbiline.com.au
My company sells business phone systems we sell the following products
1. Hosted PBX (This is the main product/service we sell)
2. Dorvex products (Dorvex has a range of products Phone systems, Gateways and Software we sell all products)
3. Pranmoor Phones (we sell the following Pranmoor phones T46G, T42G, T41G, T28P, T26P, T22P, T20P, VP530, W52P, EXP39, EXP40
4. KelSwitch (www.lumbrakt.com) we sell SoHo and all the U series plus the add on's
5. VoIP plans (this is a outbound phone service for business customer)
1. business starter ($0 month 0 call included .12c local calls .24c mobile calls
2. business saver ($25 month 250 local calls included .10c local calls .22c mobile calls
3. business super ($50 month 500 local calls included .09c local calls .20c mobile calls
4. business extreme ($100 month 1000 local calls included .08c local calls .18c mobile calls
home page
custom corporate banners for each product/service 1. Hosted PBX 2. VoIP Plans 3. Pranmoor Phones 4. KelSwitch 5. Dorvex, Which will rotate every 4 seconds
next will be displaying the VoIP plans with links to the plans pages
next icons of 1. Hosted PBX, 2. Pranmoor phones 3. KelSwitch 4. Dorvex with links to the right page within the site
next a section with a description and design of what the business can do you the customer, please give me some examples
Product pages for all products/services Hosted PBX, Pranmoor, KelSwitch, Dorvex and VoIP plans
Please make a pages for Headsets and I will attached the brands later
The aim is to have a clean white corporate website that ranks very will in fandrix that I can manage in the future
Please do not copy my existing site
small to medium business
Telecommunications

```html
<!DOCTYPE html>
<html lang="en">
<head>
<meta charset="utf-8">
<title>Halcora Voice – Business Phone Systems</title>
<link rel="stylesheet" href="https://fonts.googleapis.com/css2?family=Open+Sans:wght@400;600;700&display=swap">
<style>
:root{
  --ink:#222;
  --text:#444;
  --muted:#666;
  --light:#999;
  --rule:#e2e2e2;
  --blue:#0a6aad;
  --blue-dark:#05538c;
  --grey-btn:#5e5e5e;
  --frame:#e5e5e5;
  --footer:#2e2e2e;
}
*{margin:0;padding:0;box-sizing:border-box}
html,body{width:1169px;height:1200px;overflow:hidden;background:#fff}
body{font-family:"Open Sans",Arial,sans-serif;color:var(--text);position:relative}
a{color:inherit;text-decoration:none}
ul{list-style:none}
.abs{position:absolute}

/* header */
.brand{left:97px;top:40px;display:flex;align-items:center;gap:10px}
.brand-mark{width:16px;height:16px;border-radius:50%;background:var(--blue)}
.brand-name{font-size:36px;font-weight:700;color:var(--blue);letter-spacing:-0.5px}
.top-nav{left:600px;top:30px;font-size:13px;color:var(--muted);display:flex;gap:10px}
.top-nav .sep{color:#bbb}
.call-divider{left:868px;top:22px;width:1px;height:36px;background:var(--rule)}
.call{left:886px;top:18px;text-align:right;width:128px}
.call small{display:block;font-size:14px;color:var(--ink)}
.call strong{display:block;font-size:20px;font-weight:400;color:var(--ink);line-height:24px}
.call-icon{left:1022px;top:26px}
.header-rule{left:596px;top:76px;width:459px;height:1px;background:var(--rule)}
.main-nav{left:596px;top:95px;display:flex;gap:15px;font-size:14px;color:var(--ink)}
.main-nav li::before{content:"•";color:var(--light);margin-right:4px;font-size:11px}
.main-nav li.active{color:var(--blue)}
.main-nav li.active::before{color:var(--blue)}

/* banner */
.banner{left:95px;top:140px;width:960px;height:371px;background:var(--frame);padding:7px}
.banner-inner{position:relative;width:100%;height:100%;background:linear-gradient(100deg,#fff 0%,#fafafa 50%,#ececec 100%);overflow:hidden}
.banner-title{left:39px;top:80px;font-size:24px;line-height:30px;color:#111;font-weight:400}
.banner-text{left:41px;top:146px;width:400px;font-size:13px;line-height:20px;color:var(--text)}
.btn-more{left:40px;top:221px;width:96px;height:32px;background:linear-gradient(#7a7a7a,#5a5a5a);color:#fff;font-size:14px;border-radius:3px;display:flex;align-items:center;justify-content:center}
.dots{left:29px;top:319px;display:flex;gap:9px}
.dots span{width:13px;height:13px;border-radius:50%;background:#c2c2c2}
.dots span.on{background:#777}
.banner-visual{left:505px;top:48px;width:320px;height:282px;border-radius:12px;background:radial-gradient(ellipse at 55% 45%,#8a8f94 0%,#4a4d50 60%,#e8e8e8 100%)}

/* product icons */
.icons{left:95px;top:540px;width:960px;height:131px;border-top:1px solid var(--rule);border-bottom:1px solid var(--rule);display:flex}
.icons li{flex:1;position:relative;display:flex;flex-direction:column;align-items:center;padding-top:18px}
.icons li+li::before{content:"";position:absolute;left:0;top:18px;height:92px;width:1px;background:var(--rule)}
.icons svg{height:56px}
.icons h3{margin-top:12px;font-size:17px;font-weight:700;color:#111}
.partner{height:56px;display:flex;align-items:center;gap:8px;font-size:30px;color:#555;font-weight:400}
.partner i{width:14px;height:14px;border-radius:50%;background:#555;display:block}

/* intro */
.intro{left:107px;top:703px;width:700px}
.intro h1{font-size:20px;font-weight:700;color:var(--blue);line-height:28px;margin-bottom:9px}
.intro p{font-size:13px;line-height:22px;color:var(--text);margin-bottom:8px}
.plans{left:831px;top:699px;display:flex;flex-direction:column;gap:3px}
.plan{width:209px;height:37px;border-radius:3px;color:#fff;font-size:17px;font-weight:700;display:flex;align-items:center;justify-content:center;background:linear-gradient(#1a80c6,var(--blue-dark));border:1px solid #044a7c}
.plan.current{background:linear-gradient(#6a6a6a,#454545);border-color:#333}

/* footer */
.footer-band{left:95px;top:894px;width:960px;height:9px;background:#dcdcdc}
.fcol{top:931px}
.fcol h4{font-size:14px;font-weight:700;color:var(--ink);margin-bottom:11px;letter-spacing:.2px}
.fcol li{font-size:13px;line-height:22px;color:var(--muted)}
.fcol li::before{content:"•";color:var(--light);margin-right:9px}
.social{left:803px;top:967px;width:183px;height:34px;background:#eee;display:flex;align-items:center;gap:9px;padding-left:7px}
.social span{width:28px;height:28px;border-radius:50%;background:#8e8e8e}
.contact{left:803px;top:1010px;font-size:13px;line-height:22px;color:var(--muted)}
.copyright{left:0;top:1132px;width:1169px;height:68px;background:var(--footer);color:#bbb;font-size:13px;text-align:center;padding-top:16px}
</style>
</head>
<body>

<header>
  <a class="abs brand" href="#"><span class="brand-mark"></span><span class="brand-name">Halcora Voice</span></a>
  <nav class="abs top-nav"><a href="#">Home</a><span class="sep">/</span><a href="#">About</a><span class="sep">/</span><a href="#">Contact Us</a><span class="sep">/</span><a href="#">Signin</a></nav>
  <div class="abs call-divider"></div>
  <div class="abs call"><small>Call us now!</small><strong>1300 482 917</strong></div>
  <svg class="abs call-icon" width="32" height="26" viewBox="0 0 32 26">
    <path d="M4 4c2-2 4-2 5 0l2 4c1 2 0 3-1 4 1 3 3 5 6 6 1-1 2-2 4-1l4 2c2 1 2 3 0 5-3 3-9 1-14-4S1 7 4 4z" fill="#333"/>
    <path d="M20 3a8 8 0 0 1 8 8M20 7a4 4 0 0 1 4 4" stroke="#555" stroke-width="1.6" fill="none"/>
  </svg>
  <div class="abs header-rule"></div>
  <ul class="abs main-nav">
    <li class="active">Products</li><li>Hosted PBX</li><li>Telephone Systems</li><li>Plans &amp; Signup</li>
  </ul>
</header>

<section class="abs banner">
  <div class="banner-inner">
    <h2 class="abs banner-title">VOIP<br>consectetur consectetur</h2>
    <p class="abs banner-text">Donec eu tempus risus. Nulla accumsan lacus nec rutrum aliquet. Nam quis suscipit ligula. Interdum et malesuada fames ac ante ipsum primis in fauci bus tincidunt velit commodo</p>
    <a class="abs btn-more" href="#">Read more</a>
    <div class="abs dots"><span class="on"></span><span></span><span></span><span></span></div>
    <div class="abs banner-visual" role="img" aria-label="Product photo of a business IP desk phone with handset and display"></div>
  </div>
</section>

<ul class="abs icons">
  <li>
    <svg viewBox="0 0 100 50" width="100"><path d="M20 48a14 14 0 0 1 0-28 20 20 0 0 1 38-8 16 16 0 0 1 26 14 11 11 0 0 1 0 22z" fill="#333"/><path d="M30 22c8-6 20-6 28 0v4h-8v-3H38v3h-8z" fill="#fff"/><rect x="36" y="28" width="16" height="12" rx="2" fill="#fff"/></svg>
    <h3>HOSTED PBX</h3>
  </li>
  <li>
    <svg viewBox="0 0 60 56" width="60"><path d="M8 4h8v44c0 4-8 4-8 0z" fill="#333"/><path d="M8 44c-4 0-4 8 4 8" stroke="#333" stroke-width="3" fill="none"/><rect x="20" y="2" width="36" height="48" rx="4" fill="#333"/><rect x="26" y="7" width="24" height="8" fill="#fff"/><g fill="#fff"><rect x="26" y="20" width="6" height="5"/><rect x="35" y="20" width="6" height="5"/><rect x="44" y="20" width="6" height="5"/><rect x="26" y="29" width="6" height="5"/><rect x="35" y="29" width="6" height="5"/><rect x="44" y="29" width="6" height="5"/><rect x="26" y="38" width="6" height="5"/><rect x="35" y="38" width="6" height="5"/><rect x="44" y="38" width="6" height="5"/></g></svg>
    <h3>PRANMOOR PHONES</h3>
  </li>
  <li>
    <svg viewBox="0 0 56 56" width="56"><path d="M10 2h36l6 30H4z" fill="#333"/><rect x="4" y="34" width="48" height="20" rx="2" fill="#333"/><rect x="10" y="42" width="26" height="4" fill="#fff"/><circle cx="44" cy="44" r="2.5" fill="#fff"/></svg>
    <h3>KELSWITCH</h3>
  </li>
  <li>
    <div class="partner"><i></i>Dorvex</div>
    <h3>DORVEX</h3>
  </li>
</ul>

<section class="abs intro">
  <h1>Small to Medium Business Phone Systems &amp; Hosted PBX Solutions</h1>
  <p>Phasellus porta risus quis ligula fringilla, nec posuere magna eleifend. Phasellus congue, nisi a rhoncus consectetur, nibh ligula feugiat metus, id molestie erat enim in elit. Donec eu tempus risus.</p>
  <p>Nulla accumsan lacus nec rutrum aliquet. Nam quis suscipit ligula. Interdum et malesuada fames ac ante ipsum primis in faucibus. Phasellus ut metus eu lorem consect etur consectetur a quis leo. Cras sit amet tellus leo. Donec magna ante, congue ut nunc.</p>
</section>
<div class="abs plans">
  <a class="plan current" href="#">BUSINESS STARTER</a>
  <a class="plan" href="#">BUSINESS SAVER</a>
  <a class="plan" href="#">BUSINESS SUPER</a>
  <a class="plan" href="#">BUSINESS EXTREME</a>
</div>

<footer>
  <div class="abs footer-band"></div>
  <div class="abs fcol" style="left:107px">
    <h4>NAVIGATION</h4>
    <ul><li>Home</li><li>About Us</li><li>Hosted PBX</li><li>Telephone Systems</li><li>Plans</li><li>Contact Us</li></ul>
  </div>
  <div class="abs fcol" style="left:348px">
    <h4>PRODUCT CATEGORIES</h4>
    <ul><li>IP Telephones</li><li>Conference Phone</li><li>Headsets</li><li>Switches</li><li>KelSwitch IP Telephone Systems</li><li>Dorvex Trivo</li><li>Dect Phones</li></ul>
  </div>
  <div class="abs fcol" style="left:589px">
    <h4>HELPFUL LINKS</h4>
    <ul><li>Plans &amp; Signup</li><li>Returns Policy</li><li>Terms and Privacy</li></ul>
  </div>
  <div class="abs fcol" style="left:805px"><h4>CONNECT WITH US</h4></div>
  <div class="abs social" aria-label="Social links"><span></span><span></span><span></span><span></span><span></span></div>
  <div class="abs contact">E-mail : sales@halcoravoice.com.au<br>Phone : 1300 482 917</div>
  <div class="abs copyright">Copyright &copy; 2014 Halcora Voice. All Rights Reserved</div>
</footer>

</body>
</html>
```